Quorvex business card design

create modern and tech looking business card that is clean but effectively communciates that we are a cloud communications company.
Should have at minimum:
Employee Name
Postion
Phone Number
Email
website
create modern and tech looking business card that is clean but effectively communciates that we are a cloud communications company. We have two logo color schemes (attached) so would like to see designs both ways
Should have at minimum:
Employee Name
Postion
Phone Number
Email
website

```html
<!DOCTYPE html>
<html lang="en">
<head>
<meta charset="utf-8">
<title>Quorvex business card</title>
<link href="https://fonts.googleapis.com/css2?family=Roboto:wght@400;500;700&display=swap" rel="stylesheet">
<style>
  :root {
    --purple: #6a3194;
    --purple-dark: #552679;
    --cyan: #2dbbdc;
    --cyan-dark: #1f93b0;
    --white: #ffffff;
    --ink: #222222;
    --backdrop: #e9e9ec;
  }
  * { box-sizing: border-box; margin: 0; padding: 0; }
  html, body {
    width: 1200px; height: 900px; overflow: hidden;
    background: var(--backdrop);
    font-family: "Roboto", Arial, sans-serif;
  }
  .sheet { position: relative; width: 1200px; height: 900px; }

  .card {
    position: absolute; left: 280px; width: 640px; height: 366px;
    border-radius: 22px; overflow: hidden;
    box-shadow: 0 10px 28px rgba(0,0,0,0.18);
  }
  .card--front { top: 44px; background: var(--purple); }
  .card--back { top: 490px; background: var(--white); }

  /* wordmark */
  .wordmark {
    position: absolute; display: flex; align-items: center; gap: 14px;
    font-weight: 700; letter-spacing: 6px; text-transform: uppercase;
  }
  .wordmark__square { display: block; background: var(--cyan); }
  .card--front .wordmark {
    left: 50%; top: 140px; transform: translateX(-50%);
    color: var(--white); font-size: 58px;
  }
  .card--front .wordmark__square { width: 40px; height: 40px; }
  .front__web {
    position: absolute; right: 150px; bottom: 62px;
    color: var(--white); font-size: 15px; letter-spacing: 0.5px;
  }

  /* back */
  .back__panel {
    position: absolute; inset: 0; background: var(--purple);
    clip-path: polygon(48% 0, 100% 0, 100% 100%, 58% 100%);
  }
  .back__ribbon {
    position: absolute; top: 46px; left: 272px; width: 316px; height: 66px;
    background: var(--cyan); color: var(--white);
    display: flex; flex-direction: column; justify-content: center; align-items: center;
    clip-path: polygon(0 0, 100% 0, 93% 100%, 0 100%);
  }
  .back__ribbon-fold {
    position: absolute; top: 112px; left: 272px; width: 28px; height: 20px;
    background: var(--cyan-dark); clip-path: polygon(0 0, 100% 0, 100% 100%);
  }
  .ribbon__name { font-size: 22px; font-weight: 700; letter-spacing: 0.5px; }
  .ribbon__role { font-size: 13px; margin-top: 2px; }

  .card--back .wordmark {
    left: 40px; top: 118px; color: var(--purple); font-size: 38px; letter-spacing: 4px;
  }
  .card--back .wordmark__square { width: 26px; height: 26px; }

  .contact-list {
    position: absolute; left: 40px; bottom: 40px; list-style: none;
    display: flex; flex-direction: column; gap: 8px;
  }
  .contact-list__item { display: flex; align-items: center; gap: 12px; font-size: 17px; color: var(--ink); }
  .contact-list__icon {
    width: 26px; height: 26px; background: var(--purple);
    display: flex; align-items: center; justify-content: center;
  }
  .contact-list__icon svg { width: 15px; height: 15px; }

  .address {
    position: absolute; right: 40px; bottom: 48px; width: 230px;
    color: var(--white); font-size: 16px; line-height: 1.35; text-align: center;
  }
  .address svg { display: block; margin: 0 auto 8px; width: 16px; height: 20px; }
</style>
</head>
<body>
<main class="sheet">

  <section class="card card--front" aria-label="Card front">
    <div class="wordmark"><span class="wordmark__square"></span><span>Quorvex</span></div>
    <p class="front__web">www.yourwebname.com</p>
  </section>

  <section class="card card--back" aria-label="Card back">
    <div class="back__panel"></div>
    <div class="back__ribbon-fold"></div>
    <div class="back__ribbon">
      <span class="ribbon__name">JOHN DOE</span>
      <span class="ribbon__role">Owner</span>
    </div>

    <div class="wordmark"><span class="wordmark__square"></span><span>Quorvex</span></div>

    <ul class="contact-list">
      <li class="contact-list__item">
        <span class="contact-list__icon"><svg viewBox="0 0 24 24"><path fill="#fff" d="M6.6 10.8a15 15 0 0 0 6.6 6.6l2.2-2.2a1 1 0 0 1 1-.25 11.4 11.4 0 0 0 3.6.57 1 1 0 0 1 1 1V20a1 1 0 0 1-1 1A17 17 0 0 1 3 4a1 1 0 0 1 1-1h3.5a1 1 0 0 1 1 1c0 1.25.2 2.45.57 3.6a1 1 0 0 1-.25 1z"/></svg></span>
        123-456-1234
      </li>
      <li class="contact-list__item">
        <span class="contact-list__icon"><svg viewBox="0 0 24 24"><rect x="4" y="9" width="16" height="11" rx="2" fill="#fff"/><path d="M3 8c2-4 16-4 18 0v2h-4V8H7v2H3z" fill="#fff"/><circle cx="12" cy="14.5" r="2.5" fill="#6a3194"/></svg></span>
        111-222-3333
      </li>
      <li class="contact-list__item">
        <span class="contact-list__icon"><svg viewBox="0 0 24 24"><rect x="3" y="6" width="18" height="12" fill="none" stroke="#fff" stroke-width="2"/><path d="M3 6l9 7 9-7" fill="none" stroke="#fff" stroke-width="2"/></svg></span>
        yourmail@email.com
      </li>
      <li class="contact-list__item">
        <span class="contact-list__icon"><svg viewBox="0 0 24 24"><circle cx="12" cy="12" r="9" fill="none" stroke="#fff" stroke-width="2"/><path d="M3 12h18M12 3c3 3 3 15 0 18M12 3c-3 3-3 15 0 18" fill="none" stroke="#fff" stroke-width="1.6"/></svg></span>
        www.yourwebname.com
      </li>
    </ul>

    <address class="address" style="font-style:normal">
      <svg viewBox="0 0 16 20"><path fill="#fff" d="M8 0a7 7 0 0 0-7 7c0 5 7 13 7 13s7-8 7-13a7 7 0 0 0-7-7zm0 9.5A2.5 2.5 0 1 1 8 4.5a2.5 2.5 0 0 1 0 5z"/></svg>
      2201 Your Street Address 123<br>Burlington AA 12345
    </address>
  </section>

</main>
</body>
</html>
```